Travel Group 'Lydgate Group' needs a new business card design

Lydgate Group is a diverse business specialising in bespoke, tailor made holidays to suit all budgets and we are specialists in planning exciting day/short trips to suit all markets. Our target market is very varied going from the corporate client and as well as people in the community who simply want to experience something special.
We are looking for a card design that will encourage people to look at our websites and social media platforms and to see for themselves the different facets to our business. It is essential that the card has social media icons for Facebook, Twitter and Instagram. We are looking for a card with a blank background with no pictures and for the front side to have the attached Lydgate logo. The card should have similar colour scheme to the attached Lydgate logo.
The card must have the following information on one side:
Maud Penrose
Business Development Manager
maudpenrose@lydgatevoyages.example
Lydgate Group, 87 Quarry Lane
Braeford, Lanmuir, Scotland KA19 4TN
+44 (0)1632 730182
And then the card must have the following on the second side:
(Lydgate logo)
(social media icons)
www.lydgatevoyages.example
www.lydgateoutings.example
Target Market(s)
Our target market is very varied going from the corporate client and as well as people in the community who simply want to experience something special.
Industry/Entity Type
Business
Contact Information for Business Card
Maud Penrose
+44 (0)1632 730182
(Lydgate logo)
(social media icons)
www.lydgatevoyages.example
www.lydgateoutings.example
Requirements
Must have
- It is essential that the card has social media icons for Facebook, Twitter & Instagram.
Should not have
- Should not have any images other than Lydgate logo.

```html
<!DOCTYPE html>
<html lang="en">
<head>
<meta charset="utf-8">
<title>Lydgate Group – Business Card</title>
<link rel="stylesheet" href="https://fonts.googleapis.com/css2?family=Tinos:wght@700&family=Lato:wght@400&display=swap">
<style>
  :root {
    --backdrop-top: #262626;
    --backdrop-bottom: #050505;
    --card-white: #ffffff;
    --brand-navy: #2b2466;
    --brand-navy-deep: #1e1850;
    --ink: #2a2a2a;
    --social-a: #3b5998;
    --social-b: #55acee;
    --social-c: #3f729b;
  }
  * { box-sizing: border-box; margin: 0; padding: 0; }
  html, body {
    width: 1200px; height: 900px; overflow: hidden;
    background: linear-gradient(180deg, var(--backdrop-top) 0%, var(--backdrop-bottom) 100%);
  }
  .stage { position: relative; width: 1200px; height: 900px; }
  .card {
    position: absolute; top: 306px; height: 271px;
    background: var(--card-white); border-radius: 10px; overflow: hidden;
  }
  .card--contact { left: 149px; width: 439px; }
  .card--brand { left: 608px; width: 441px; }

  .card__header {
    height: 92px; background: var(--brand-navy);
    border-bottom: 2px solid var(--brand-navy-deep);
    padding: 24px 0 0 22px;
  }
  .card__wordmark {
    font-family: "Tinos", "Times New Roman", serif; font-weight: 700;
    font-size: 44px; letter-spacing: 2px; color: var(--card-white); line-height: 1;
  }
  .card__body { padding: 16px 0 0 22px; font-family: "Lato", sans-serif; color: var(--ink); }
  .person__name {
    font-family: "Tinos", "Times New Roman", serif; font-weight: 700;
    font-size: 16px; letter-spacing: 0.5px; color: var(--brand-navy); line-height: 18px;
  }
  .person__role { font-size: 12.5px; line-height: 16px; margin-bottom: 6px; }
  .contact-list { list-style: none; font-size: 12px; line-height: 16px; }
  .contact-list li { display: flex; align-items: center; gap: 5px; }
  .contact-list svg { width: 9px; height: 9px; fill: var(--brand-navy); flex: none; }
  .address { font-size: 12px; line-height: 16px; margin-top: 6px; }

  .social { position: absolute; left: 340px; bottom: 32px; display: flex; gap: 7px; }
  .social span { width: 20px; height: 20px; display: block; }
  .social .social--a { background: var(--social-a); }
  .social .social--b { background: var(--social-b); }
  .social .social--c { background: var(--social-c); }

  .brand-lockup {
    position: absolute; left: 0; right: 0; top: 149px;
    text-align: center; padding-left: 40px;
    font-family: "Tinos", "Times New Roman", serif; font-weight: 700;
    font-size: 27px; letter-spacing: 2px; color: var(--brand-navy); line-height: 1;
  }
</style>
</head>
<body>
<main class="stage">
  <section class="card card--contact" aria-label="Card back with contact details">
    <header class="card__header">
      <h1 class="card__wordmark">LYDGATE</h1>
    </header>
    <div class="card__body">
      <h2 class="person__name">MAUD PENROSE</h2>
      <p class="person__role">Business Development Manager</p>
      <ul class="contact-list">
        <li><svg viewBox="0 0 10 10" aria-hidden="true"><path d="M1 3c0-1 1-2 4-2s4 1 4 2v1H7V3H3v1H1zM2 5h6l1 4H1z"/></svg>+44 (0)1632 730182</li>
        <li><svg viewBox="0 0 10 10" aria-hidden="true"><path d="M0 2h10v6H0zM1 3v.4L5 6l4-2.6V3L5 5.5z" fill-rule="evenodd"/></svg>maudpenrose@lydgatevoyages.example</li>
        <li><svg viewBox="0 0 10 10" aria-hidden="true"><circle cx="5" cy="5" r="4.5"/></svg>www.lydgatevoyages.example</li>
        <li><svg viewBox="0 0 10 10" aria-hidden="true"><circle cx="5" cy="5" r="4.5"/></svg>www.lydgateoutings.example</li>
      </ul>
      <p class="address">Lydgate Group, 87 Quarry Lane<br>Braeford, Lanmuir, Scotland KA19 4TN</p>
    </div>
    <div class="social" aria-label="Social media">
      <span class="social--a"></span>
      <span class="social--b"></span>
      <span class="social--c"></span>
    </div>
  </section>

  <section class="card card--brand" aria-label="Card front with brand name">
    <p class="brand-lockup">LYDGATE</p>
  </section>
</main>
</body>
</html>
```